Form Crafters Business Card

Professional cosmetic surgery company, based in very exclusive area in London. High profiled clientele. Brand is very artistic, modern, state-of-the-art, safe. The best in the business. Celebrity clientele.

Form Crafter’s of London is a brand serving a discriminating and exclusive clientele who value personal service that is both intimate and high end. Our clients choose Form Crafters because of the relationships we share with all of our customers. The clients of Form Crafters have an equal partnership between customers, and very experienced, highly qualified medical professionals. This together provides you with a professional service that keeps you looking good and feeling good. It is a relationship based on honesty, compassion, loyalty and respect.
Form Crafter’s have provided services for internationally recognised celebrities, and other high profiled individuals.

The cards are used for networking at private, exclusive events with VIPs.

Target Market(s)

Professionals
Rich people

Industry/Entity Type

Professional Service

Contact Information for Business Card

Need double sided business card design for 4 people. Back of the business card needs to have contrast background to the front with butterfly watermark with services provided:
Hair Restoration surgery
Hair Loss treatments
Breast surgery
Rhinoplasty
Zelix Liposuction
Fat Grafting
Lumex & Fillers

Front of the business card needs to be a nice satin black.
with following information:
Talvan Desoruthy - name
Chief Executive - Job title

www.formcrafters-example.co.uk
talvan@formcrafters-example.co.uk
Phone: +44 (0)207 146 5327
Mobile: +44 (0)7491 825 436

The London Calder Infirmary
14 Pellmont Street | London | W1K 3TR
Off Dunmore Lane

All business cards have the same address, phone, website as Talvan's details.
Same details on the back of the business card as well.
The other cards have different name, job title, email, mobile number

Kerem Lutz - Name
Partner - Job Title
Former England International Cricketer - please include below job title

email: kerem@formcrafters-example.co.uk
mobile: +44(0)7862 514208

Dr Stellan Vastrel - Name
Plastic Surgeon - Job Title
drvastrel@formcrafters-example.co.uk
No mobile number

Dr Jon Torvick FRCS (please put FRCS in small font) - Name
Hair Restoration Surgeon - Job Title
drtorvick@formcrafters-example.co.uk
No mobile number

Colors
cedeec
85abd2
0655a3

Requirements
Must have
• The logo needs to be in a metallic finish
• Text needs to be striking
• nice background
• butterfly watermark on the back

```html
<!DOCTYPE html>
<html lang="en">
<head>
<meta charset="utf-8">
<title>Form Crafters Business Card</title>
<link rel="stylesheet" href="https://fonts.googleapis.com/css2?family=Cinzel:wght@400;700&display=swap">
<style>
  :root {
    --page: #e4e4e4;
    --card: #1d1e20;
    --card-back: #161718;
    --blue: #1f8fd0;
    --blue-deep: #0655a3;
    --orange: #f0522a;
    --amber: #f5a623;
    --silver: #d8dadc;
    --silver-soft: #b9bcc0;
  }
  * { box-sizing: border-box; margin: 0; padding: 0; }
  html, body { width: 1200px; height: 720px; overflow: hidden; background: var(--page); }
  body { position: relative; font-family: "Cinzel", serif; }

  .card {
    position: absolute;
    top: 242px;
    width: 420px;
    height: 240px;
    overflow: hidden;
  }
  .card--front { left: 147px; background: linear-gradient(135deg, #242527, var(--card) 60%, #18191a); }
  .card--back { left: 633px; background: radial-gradient(ellipse at 50% 35%, #2a2b2d, var(--card-back) 70%); }

  .brand {
    position: absolute;
    font-weight: 400;
    letter-spacing: 0.5px;
    white-space: nowrap;
    display: flex;
    align-items: center;
    gap: 7px;
  }
  .brand__dot { width: 9px; height: 9px; border-radius: 50%; }
  .card--front .brand { left: 17px; top: 34px; font-size: 20px; color: var(--blue); }
  .card--front .brand__dot { background: var(--orange); }
  .card--back .brand { left: 0; right: 0; top: 86px; justify-content: center; font-size: 25px; color: var(--silver); }
  .card--back .brand__dot { background: var(--silver-soft); }

  .watermark {
    position: absolute;
    left: 300px; top: 0;
    width: 110px; height: 150px;
    border-radius: 50% 50% 40% 40%;
    background: radial-gradient(ellipse at 45% 40%, rgba(240,120,60,0.12), rgba(40,110,170,0.10) 60%, transparent 75%);
  }

  .person { position: absolute; left: 17px; top: 82px; }
  .person__name { font-weight: 700; font-size: 13.5px; color: var(--orange); letter-spacing: 0.3px; }
  .person__title { font-size: 10.5px; color: var(--blue); margin-top: 1px; }

  .address { position: absolute; left: 17px; top: 125px; font-size: 10px; line-height: 12px; color: var(--blue); }

  .contacts { position: absolute; left: 17px; top: 176px; list-style: none; font-size: 10px; line-height: 12px; color: var(--blue); }
  .contacts li { display: flex; align-items: center; gap: 9px; }
  .contacts svg { width: 10px; height: 9px; flex: none; }

  .stripe { position: absolute; bottom: 0; }
  .stripe--blue { left: 0; width: 276px; height: 7px; background: linear-gradient(90deg, var(--blue-deep), var(--blue)); clip-path: polygon(0 0, 100% 0, 98% 100%, 0 100%); }
  .stripe--orange { left: 276px; width: 144px; height: 17px; background: linear-gradient(90deg, var(--orange), var(--amber)); clip-path: polygon(7% 0, 100% 0, 100% 100%, 0 100%); }

  .services {
    position: absolute; left: 0; right: 0; top: 172px;
    text-align: center; list-style: none;
    font-size: 10.5px; line-height: 12px; color: var(--silver);
    text-shadow: 0 1px 1px rgba(0,0,0,0.8);
  }
</style>
</head>
<body>
  <section class="card card--front">
    <div class="watermark" role="img" aria-label="Faint butterfly watermark"></div>
    <div class="brand"><span class="brand__dot"></span>Form Crafters</div>
    <div class="person">
      <p class="person__name">Talvan Desoruthy</p>
      <p class="person__title">Chief Executive</p>
    </div>
    <p class="address">The London Calder Infirmary<br>14 Pellmont Street | London |<br>W1K 3TR Off Dunmore Lane</p>
    <ul class="contacts">
      <li><svg viewBox="0 0 10 9"><path d="M1 3 Q5 0 9 3 L8 4 L6 3 L6 2 L4 2 L4 3 L2 4 Z M2 5 H8 V8 H2 Z" fill="var(--orange)"/></svg>+44 (0)207 146 5327</li>
      <li><svg viewBox="0 0 10 9"><rect x="3" y="0.5" width="4" height="8" rx="1" fill="none" stroke="var(--orange)"/></svg>+44 (0)7491 825 436</li>
      <li><svg viewBox="0 0 10 9"><rect x="0.5" y="1" width="9" height="7" fill="var(--orange)"/><path d="M0.5 1 L5 5 L9.5 1" fill="none" stroke="var(--card)"/></svg>talvan@formcrafters-example.co.uk</li>
      <li><svg viewBox="0 0 10 9"><rect x="1" y="1" width="8" height="5.5" fill="none" stroke="var(--orange)"/><path d="M3 8.5 H7" stroke="var(--orange)"/></svg>www.formcrafters-example.co.uk</li>
    </ul>
    <div class="stripe stripe--blue"></div>
    <div class="stripe stripe--orange"></div>
  </section>

  <section class="card card--back">
    <div class="brand"><span class="brand__dot"></span>Form Crafters</div>
    <ul class="services">
      <li>Hair Restoration surgery</li>
      <li>Hair Loss treatments</li>
      <li>Breast surgery Rhinoplasty Zelix</li>
      <li>Liposuction Fat Grafting Lumex &amp; Fillers</li>
    </ul>
  </section>
</body>
</html>
```